Digital content business needs banner ads

We sell content - if you need an article to put on your website or in a newsletter, you can purchase a ready made article from us and edit it to your liking to use straight away. This could be any kind of article, but this banner ad will be aimed at real estate agents. You can see the website (and the style of articles) here https://www.thebluelanternpost.com.au
The banner is meant to solve the problem of the front desk admin or agent trying to think of something to write to put in their email newsletter. This will save them time as they can just select an article from our library and use it (for a fee of course!).
Needs to have the words:
--------------------------------------------------
Find the next article for your newsletter
---------------------------------------------------
Some imagery would be good rather than plain text.
With a call to action like click here button or similar
Required sizes (or provide a set of standard sized ads):
728 x 90
970 x 250
300x250
Real Estate Agents

```html
<!DOCTYPE html>
<html lang="en">
<head>
<meta charset="utf-8">
<title>Blue Lantern Post – Banner Set</title>
<link rel="stylesheet" href="https://fonts.googleapis.com/css2?family=Poppins:wght@500;600;700;800&display=swap">
<style>
  :root {
    --navy: #0b3a74;
    --blue: #1d9be6;
    --sky: #5fc8f5;
    --banner-top: #2e87c9;
    --white: #ffffff;
    --ink: #0a0a0a;
    --photo-light: #eceff1;
    --photo-mid: #d9cfc4;
    --photo-warm: #b86a66;
  }
  * { box-sizing: border-box; margin: 0; padding: 0; }
  html, body { width: 1200px; height: 1124px; overflow: hidden; background: var(--white); }
  body { position: relative; font-family: "Poppins", sans-serif; }

  .banner { position: absolute; overflow: hidden; background: var(--white);
    box-shadow: 0 2px 8px rgba(0,0,0,0.12); }
  .banner .scene { position: absolute; inset: 0; width: 100%; height: 100%; }

  .size-label { position: absolute; color: var(--navy); font-weight: 600; font-size: 45px; line-height: 1; }
  .set-title { position: absolute; left: 589px; top: 734px; color: var(--navy);
    font-weight: 600; font-size: 46px; line-height: 46px; }

  .brand { position: absolute; display: flex; align-items: center; color: var(--navy);
    font-weight: 700; line-height: 1.05; }
  .brand-square { flex: none; background: var(--blue); }

  .cta { position: absolute; display: flex; align-items: center; justify-content: center;
    background: var(--blue); color: var(--white); font-weight: 600; border-radius: 6px; line-height: 1; }

  .kicker { position: absolute; white-space: nowrap; font-weight: 600; line-height: 1; }
  .kicker strong { font-weight: 800; }
  .headline { position: absolute; white-space: nowrap; font-weight: 800; line-height: 1; }

  /* 970 x 250 */
  .banner-wide { left: 40px; top: 43px; width: 1120px; height: 288px;
    background: linear-gradient(180deg, var(--banner-top) 0%, #7fb9e2 40%, var(--white) 68%); }
  .banner-wide .kicker { left: 24px; top: 26px; color: var(--white); font-size: 28px; }
  .banner-wide .kicker strong { font-size: 44px; }
  .banner-wide .headline { left: 24px; top: 67px; color: var(--navy); font-size: 80px; letter-spacing: 1px; }
  .banner-wide .brand { left: 28px; top: 190px; width: 150px; font-size: 20px; gap: 10px; }
  .banner-wide .brand-square { width: 24px; height: 24px; }
  .banner-wide .cta { left: 220px; top: 171px; width: 245px; height: 59px; font-size: 23px; }

  /* 728 x 90 */
  .banner-leader { left: 40px; top: 440px; width: 772px; height: 95px; }
  .banner-leader .brand { left: 8px; top: 14px; width: 90px; font-size: 12px; gap: 5px; }
  .banner-leader .brand-square { width: 12px; height: 12px; }
  .banner-leader .cta { left: 8px; top: 72px; width: 88px; height: 19px; font-size: 8px; border-radius: 4px; }
  .banner-leader .kicker { left: 121px; top: 14px; color: var(--blue); font-size: 17px; }
  .banner-leader .kicker strong { font-size: 33px; }
  .banner-leader .headline { left: 118px; top: 44px; color: var(--navy); font-size: 50px; letter-spacing: 3px; }

  /* 300 x 250 */
  .banner-square { left: 33px; top: 640px; width: 480px; height: 399px; }
  .banner-square .brand { left: 15px; top: 32px; width: 180px; font-size: 26px; gap: 10px; }
  .banner-square .brand-square { width: 28px; height: 28px; }
  .banner-square .kicker { left: 12px; top: 181px; color: var(--navy); font-size: 25px; }
  .banner-square .accent { position: absolute; left: 12px; top: 208px; white-space: nowrap;
    color: var(--blue); font-weight: 800; font-size: 55px; line-height: 1; }
  .banner-square .accent span { font-size: 28px; font-weight: 700; margin-left: 21px; }
  .banner-square .headline { left: 12px; top: 264px; color: var(--ink); font-size: 54px; letter-spacing: 2px; }
  .banner-square .cta { left: 17px; top: 335px; width: 163px; height: 44px; font-size: 16px; border-radius: 8px; }
</style>
</head>
<body>

  <section class="banner banner-wide">
    <svg class="scene" viewBox="0 0 1120 288" preserveAspectRatio="none">
      <defs>
        <linearGradient id="photoWide" x1="0" y1="0" x2="1" y2="0">
          <stop offset="0" stop-color="var(--photo-light)"/>
          <stop offset="0.6" stop-color="var(--photo-mid)"/>
          <stop offset="1" stop-color="var(--photo-warm)"/>
        </linearGradient>
        <linearGradient id="arcWide" x1="0" y1="0" x2="0" y2="1">
          <stop offset="0" stop-color="var(--blue)"/><stop offset="1" stop-color="var(--sky)"/>
        </linearGradient>
      </defs>
      <path d="M666,0 Q502,150 654,288" fill="none" stroke="url(#arcWide)" stroke-width="6"/>
      <path d="M674,0 Q512,150 662,288 L1120,288 L1120,0 Z" fill="url(#photoWide)"
            role="img" aria-label="Photo: frustrated young man at a desk with laptop, plant and crumpled paper"/>
    </svg>
    <p class="kicker">Find the next <strong>ARTICLE</strong> for your</p>
    <h1 class="headline">NEWSLETTER</h1>
    <div class="brand"><span class="brand-square"></span>The Blue Lantern Post</div>
    <a class="cta">CONTACT US</a>
  </section>
  <p class="size-label" style="left:67px; top:377px;">970-250</p>

  <section class="banner banner-leader">
    <svg class="scene" viewBox="0 0 772 95" preserveAspectRatio="none">
      <defs>
        <linearGradient id="photoLeader" x1="0" y1="0" x2="1" y2="0">
          <stop offset="0" stop-color="var(--photo-light)"/>
          <stop offset="0.6" stop-color="var(--photo-mid)"/>
          <stop offset="1" stop-color="var(--photo-warm)"/>
        </linearGradient>
      </defs>
      <path d="M521,0 Q465,47 493,95" fill="none" stroke="var(--blue)" stroke-width="3"/>
      <path d="M525,0 Q469,47 497,95 L772,95 L772,0 Z" fill="url(#photoLeader)"
            role="img" aria-label="Photo: frustrated young man at a desk with laptop"/>
    </svg>
    <div class="brand"><span class="brand-square"></span>The Blue Lantern Post</div>
    <a class="cta">CONTACT US</a>
    <p class="kicker">Find the next <strong>ARTICLE</strong> for your</p>
    <h2 class="headline">NEWSLETTER</h2>
  </section>
  <p class="size-label" style="left:61px; top:580px;">728-90</p>

  <section class="banner banner-square">
    <svg class="scene" viewBox="0 0 480 399" preserveAspectRatio="none">
      <defs>
        <linearGradient id="photoSquare" x1="0" y1="0" x2="1" y2="0">
          <stop offset="0" stop-color="var(--photo-light)"/>
          <stop offset="0.5" stop-color="var(--photo-mid)"/>
          <stop offset="1" stop-color="var(--photo-warm)"/>
        </linearGradient>
        <linearGradient id="arcSquare" x1="0" y1="0" x2="0" y2="1">
          <stop offset="0" stop-color="var(--blue)"/><stop offset="1" stop-color="var(--sky)"/>
        </linearGradient>
      </defs>
      <path d="M291,0 Q72,196 337,399" fill="none" stroke="url(#arcSquare)" stroke-width="8"/>
      <path d="M299,0 Q82,196 345,399 L480,399 L480,0 Z" fill="url(#photoSquare)"
            role="img" aria-label="Photo: frustrated young man in checked shirt at a desk"/>
    </svg>
    <div class="brand"><span class="brand-square"></span>The Blue Lantern Post</div>
    <p class="kicker">Find the next</p>
    <p class="accent">ARTICLE<span>for your</span></p>
    <h2 class="headline">NEWSLETTER</h2>
    <a class="cta">CONTACT US</a>
  </section>
  <p class="size-label" style="left:39px; top:1062px;">300-250</p>

  <p class="set-title">3 Sized<br>Banner Design</p>

</body>
</html>
```